Corvanta512 Business Card Redesign

I want to create a design for brand new business cards, I need something exceptional for clear plastic business card design. Please do not submit without it being on a clear design. Photos of the various logo versions attached.

```html
<!DOCTYPE html>
<html lang="en">
<head>
<meta charset="UTF-8">
<title>Corvanta512 – Clear Business Card</title>
<link href="https://fonts.googleapis.com/css2?family=Montserrat:wght@400;600&display=swap" rel="stylesheet">
<style>
  :root {
    --backdrop: #c9c8cc;
    --card-fill: rgba(236, 236, 240, 0.55);
    --card-edge: rgba(255, 255, 255, 0.85);
    --band: #5a5a5c;
    --ink: #4a4a4d;
    --ink-soft: #6b6b6f;
    --brand: #2f3f72;
  }
  * { margin: 0; padding: 0; box-sizing: border-box; }
  html, body {
    width: 1200px; height: 1000px; overflow: hidden;
    background: var(--backdrop);
    font-family: "Montserrat", sans-serif;
  }
  .stage {
    position: relative; width: 1200px; height: 1000px;
    display: flex; align-items: center; justify-content: center;
  }
  .clear-card {
    position: relative; width: 360px; height: 620px;
    border-radius: 18px;
    background: var(--card-fill);
    border: 1.5px solid var(--card-edge);
    overflow: hidden;
  }
  .card-bands { position: absolute; inset: 0; }
  .brand-mark {
    position: absolute; top: 112px; left: 112px;
    display: flex; align-items: center; gap: 10px;
  }
  .brand-dot { width: 16px; height: 16px; border-radius: 50%; background: var(--brand); }
  .brand-word { font-weight: 600; font-size: 22px; color: var(--brand); }
  .identity { position: absolute; top: 250px; left: 108px; }
  .identity-name { font-weight: 600; font-size: 19px; color: var(--ink); letter-spacing: 0.5px; }
  .identity-tagline { font-size: 14px; color: var(--ink-soft); margin-top: 2px; }
  .contact-list { list-style: none; margin-top: 16px; margin-left: 14px; }
  .contact-item {
    display: flex; align-items: center; gap: 10px;
    font-size: 12.5px; color: var(--ink-soft); margin-bottom: 8px;
  }
  .contact-icon { width: 13px; height: 13px; flex: none; }
</style>
</head>
<body>
<main class="stage">
  <article class="clear-card">
    <svg class="card-bands" viewBox="0 0 360 620" width="360" height="620" aria-hidden="true">
      <path d="M190 0 C 100 70 62 190 62 320 C 62 440 76 540 96 620" fill="none" stroke="var(--band)" stroke-width="8"/>
      <path d="M356 230 C 352 390 300 520 252 620 L 204 620 C 264 510 322 400 356 230 Z" fill="var(--band)"/>
    </svg>

    <div class="brand-mark">
      <span class="brand-dot"></span>
      <span class="brand-word">Corvanta512</span>
    </div>

    <section class="identity">
      <h1 class="identity-name">CORVANTA512</h1>
      <p class="identity-tagline">Complete care</p>
      <ul class="contact-list">
        <li class="contact-item">
          <svg class="contact-icon" viewBox="0 0 16 16"><path d="M3 1h3l1.5 4-2 1.2a9 9 0 0 0 4.3 4.3L11 8.5l4 1.5v3a2 2 0 0 1-2 2C7 15 1 9 1 3a2 2 0 0 1 2-2z" fill="var(--ink)"/></svg>
          <span>555 014 2398</span>
        </li>
        <li class="contact-item">
          <svg class="contact-icon" viewBox="0 0 16 16"><rect x="1" y="3" width="14" height="10" rx="1" fill="var(--ink)"/><path d="M1.5 4 8 9l6.5-5" fill="none" stroke="#e4e4e8" stroke-width="1.3"/></svg>
          <span>hello@corvanta512.com</span>
        </li>
        <li class="contact-item">
          <svg class="contact-icon" viewBox="0 0 16 16" fill="none" stroke="var(--ink)" stroke-width="1.3"><circle cx="8" cy="8" r="6.5"/><ellipse cx="8" cy="8" rx="3" ry="6.5"/><path d="M1.5 8h13"/></svg>
          <span>corvanta512.com</span>
        </li>
      </ul>
    </section>
  </article>
</main>
</body>
</html>
```